International Clinical Software Company needs a new business card design

We are looking for a new business card design for our company that has recently expanded into the UK market, making us a multinational company.
After having rebranded our website and produced a new style guide, we are looking for a business card that is creative and attention grabbing, while being consistent with the style and colour scheme used on the new website, www.brookvale.example
We produce care management technology for the aged care market, but the main aspect we aim to communicate is the human element of our software, and the way it assists in providing better care for aged people, and stronger relationships between aged people and the staff that care for them.
Our current business card is a dark green with gold text, which makes the text quite difficult to read, not very aesthetically appealing and the colour scheme looks quite dated.
We would like something fresh and modern, that can still be colourful but doesn't use large blocks of dark colour, and uses the colours within our logo.
Something tying in with the leaves that are used in our logo could work quite nicely, along with the Autumn/Fall colours of soft greens, yellows and reds (also in our existing logo). However also happy to look at fresh, completely out of the box ideas we may not have yet considered.
Target Market(s)
The people that receive this business card work in the aged card or health industry and are either corporate/management level staff or clinical (Registered Nurses, care workers etc.)
Industry/Entity Type
Health Product
Contact Information for Business Card
Company Name - BrookvaleTech
Company locations: United Kingdom, Australia, New Zealand
Staff Details:
Staff name: Dermot Quill
Staff job title: Executive Chairman
Staff email: d.quill@brookvale.example
Office phone number: 01632 960418
Font styles to use
Other font styles liked:
- Calibri
Requirements
Must have
- Must include the BrookvaleTech brand name in it's current font
- Must include logo (3 leaves in gold circle)
- Must include Business Card Details
Nice to have
- Elements of gold
- White space
- Something autumn themed but not too cliched
Should not have
- No blue - used by a major competitor and we would like to differentiate from them
- Large blocks of dark green colour (the green that appears in our leaves on the logo on our current business card is the background colour and it is far too dark)

```html
<!DOCTYPE html>
<html lang="en">
<head>
<meta charset="utf-8">
<title>BrookvaleTech – Business Card</title>
<link href="https://fonts.googleapis.com/css2?family=Lato:ital,wght@0,300;0,400;0,700;1,700&display=swap" rel="stylesheet">
<style>
  :root {
    --page-bg: #ece7de;
    --cream: #fbf7e6;
    --pale-green: #e6efb8;
    --lime: #d9e58a;
    --yellow: #f2c531;
    --amber: #eea51d;
    --orange: #e9751c;
    --rust: #c9521e;
    --gold: #a38b64;
    --gold-soft: #c9b791;
    --taupe: #7b6d58;
    --olive: #5f6f22;
    --leaf-green: #4f8a22;
  }
  html, body {
    margin: 0;
    padding: 0;
    width: 1200px;
    height: 900px;
    overflow: hidden;
    background: var(--page-bg);
    font-family: "Lato", "Carlito", sans-serif;
  }
  .card {
    position: absolute;
    left: 75px;
    top: 150px;
    width: 1050px;
    height: 600px;
    overflow: hidden;
    box-shadow: 0 10px 30px rgba(60, 45, 20, 0.25);
    background:
      radial-gradient(ellipse 32% 38% at 52% 48%, var(--cream) 0%, rgba(251,247,230,0) 100%),
      radial-gradient(ellipse 30% 40% at 72% 78%, var(--pale-green) 0%, rgba(230,239,184,0) 100%),
      radial-gradient(ellipse 28% 30% at 40% 18%, var(--lime) 0%, rgba(217,229,138,0) 100%),
      radial-gradient(ellipse 30% 45% at 0% 30%, var(--orange) 0%, rgba(233,117,28,0) 100%),
      radial-gradient(ellipse 28% 40% at 5% 95%, var(--amber) 0%, rgba(238,165,29,0) 100%),
      radial-gradient(ellipse 30% 40% at 100% 85%, var(--orange) 0%, rgba(233,117,28,0) 100%),
      radial-gradient(ellipse 25% 35% at 95% 10%, var(--yellow) 0%, rgba(242,197,49,0) 100%),
      radial-gradient(ellipse 22% 30% at 88% 40%, var(--rust) 0%, rgba(201,82,30,0) 100%),
      linear-gradient(120deg, var(--amber) 0%, var(--pale-green) 45%, var(--cream) 60%, var(--yellow) 100%);
  }
  .brand-dot {
    position: absolute;
    left: 575px;
    top: 110px;
    width: 140px;
    height: 140px;
    border-radius: 50%;
    background: var(--gold-soft);
  }
  .content {
    position: absolute;
    left: 235px;
    top: 258px;
  }
  .brand-name {
    margin: 0;
    font-weight: 300;
    font-size: 88px;
    line-height: 1;
    color: var(--gold);
    letter-spacing: 1px;
  }
  .locations {
    margin: 14px 0 0;
    font-size: 18px;
    letter-spacing: 1.5px;
    text-transform: uppercase;
    color: var(--taupe);
    word-spacing: 4px;
  }
  .locations .sep { color: var(--gold); padding: 0 10px; }
  .tagline {
    margin: 18px 0 0;
    font-size: 26px;
    font-weight: 700;
    font-style: italic;
    color: var(--olive);
  }
  .person-name {
    margin: 14px 0 0;
    font-size: 28px;
    font-weight: 700;
    color: var(--leaf-green);
  }
  .person-title {
    margin: 2px 0 0;
    font-size: 20px;
    color: var(--olive);
  }
  .contact {
    margin: 16px 0 0;
    padding: 0;
    list-style: none;
    font-size: 20px;
    line-height: 1.5;
    color: var(--leaf-green);
  }
</style>
</head>
<body>
  <main class="card">
    <div class="brand-dot" aria-hidden="true"></div>
    <div class="content">
      <h1 class="brand-name">BrookvaleTech</h1>
      <p class="locations">United Kingdom<span class="sep">•</span>New Zealand<span class="sep">•</span>Australia</p>
      <p class="tagline">Clinical software specialists</p>
      <p class="person-name">Dermot Quill</p>
      <p class="person-title">Executive Chairman</p>
      <ul class="contact">
        <li>Office: 01632 960418</li>
        <li>Email: d.quill@brookvale.example</li>
      </ul>
    </div>
  </main>
</body>
</html>
```